Email Signature

Our company is having its 10th anniversary in 2021. We would like a new email signature to celebrate the occasion. Attached is our business card design.
Please refer to our website for actual contact details.
www.tarvinestates.com.au

Industry/Entity Type

Real Estate

Requirements
Must have
• Our logo
Email
Contact Numbers
Address
Website address

Celebrating 10 years in 2021
Nice to have
• Something that blends the designs of our website and business card

```html
<!DOCTYPE html>
<html lang="en">
<head>
<meta charset="utf-8">
<title>Tarvin Estates – Email Signature</title>
<link rel="stylesheet" href="https://fonts.googleapis.com/css2?family=Arimo:wght@400;700&display=swap">
<style>
  :root {
    --brand-blue: #1f63ad;
    --brand-blue-light: #2f74bf;
    --ink: #1d1d1d;
    --paper: #ffffff;
    --backdrop: #2a2a2a;
    --rule: #333333;
  }
  * { margin: 0; padding: 0; box-sizing: border-box; }
  html, body {
    width: 1200px;
    height: 900px;
    overflow: hidden;
    background: var(--backdrop);
    font-family: "Arimo", Arial, sans-serif;
  }
  .signature {
    position: absolute;
    left: 50px;
    top: 293px;
    width: 1100px;
    height: 313px;
    background: var(--paper);
    color: var(--ink);
  }
  .skyline-band {
    position: absolute;
    left: 0; top: 0;
    width: 100%;
    height: 72px;
    background: linear-gradient(180deg, var(--brand-blue) 0%, var(--brand-blue-light) 100%);
  }
  .brand {
    position: absolute;
    left: 30px;
    top: 110px;
    width: 310px;
    text-align: center;
  }
  .anniversary {
    display: inline-block;
    padding: 8px 14px;
    border: 2px solid var(--brand-blue);
    font-size: 17px;
    font-weight: 700;
    letter-spacing: 0.5px;
    color: var(--brand-blue);
    white-space: nowrap;
  }
  .company-name {
    margin-top: 34px;
    font-size: 31px;
    font-weight: 700;
    letter-spacing: 0.5px;
    color: var(--brand-blue);
    white-space: nowrap;
  }
  .divider {
    position: absolute;
    top: 103px;
    width: 2px;
    height: 147px;
    background: var(--rule);
  }
  .divider--first { left: 360px; }
  .divider--second { left: 711px; }
  .person {
    position: absolute;
    left: 398px;
    top: 116px;
  }
  .person__name {
    font-size: 31px;
    font-weight: 700;
    color: var(--brand-blue);
    line-height: 36px;
    white-space: nowrap;
  }
  .person__role {
    font-size: 20px;
    line-height: 24px;
  }
  .person__address {
    margin-top: 10px;
    font-size: 20px;
    line-height: 27px;
    font-style: normal;
  }
  .contacts {
    position: absolute;
    left: 748px;
    top: 121px;
    list-style: none;
  }
  .contacts__item {
    display: flex;
    align-items: center;
    height: 28px;
    font-size: 21px;
    white-space: nowrap;
  }
  .contacts__icon {
    width: 17px;
    height: 17px;
    margin-right: 10px;
    fill: var(--brand-blue);
    flex: none;
  }
  .footer-rule {
    position: absolute;
    left: 34px;
    top: 268px;
    width: 1030px;
    height: 2px;
    background: var(--rule);
  }
  .services {
    position: absolute;
    left: 0;
    top: 278px;
    width: 100%;
    text-align: center;
    font-size: 22px;
    letter-spacing: 0.3px;
  }
</style>
</head>
<body>
  <section class="signature">
    <div class="skyline-band" role="img" aria-label="City skyline silhouette in blue across the top edge"></div>

    <div class="brand">
      <div class="anniversary">Celebrating 10 years in 2021</div>
      <div class="company-name">TARVIN ESTATES</div>
    </div>

    <div class="divider divider--first"></div>

    <div class="person">
      <div class="person__name">Daniel K, Marlow</div>
      <div class="person__role">Owner</div>
      <address class="person__address">Shop 7 / 18 Harbourview Road<br>Meadowbank, NSW 2114</address>
    </div>

    <div class="divider divider--second"></div>

    <ul class="contacts">
      <li class="contacts__item">
        <svg class="contacts__icon" viewBox="0 0 24 24"><path d="M6.6 10.8c1.4 2.8 3.8 5.1 6.6 6.6l2.2-2.2c.3-.3.7-.4 1-.2 1.1.4 2.3.6 3.6.6.6 0 1 .4 1 1V20c0 .6-.4 1-1 1C10.6 21 3 13.4 3 4c0-.6.4-1 1-1h3.5c.6 0 1 .4 1 1 0 1.3.2 2.5.6 3.6.1.3 0 .7-.2 1L6.6 10.8z"/></svg>
        1300 00TARV(8278)
      </li>
      <li class="contacts__item">
        <svg class="contacts__icon" viewBox="0 0 24 24"><path d="M7 2h10v6H7z"/><path d="M4 9h16a2 2 0 0 1 2 2v7h-4v4H6v-4H2v-7a2 2 0 0 1 2-2zm4 7v4h8v-4z"/></svg>
        8123 4690
      </li>
      <li class="contacts__item">
        <svg class="contacts__icon" viewBox="0 0 24 24"><path d="M2 5h20v14H2V5zm2 2v.4l8 5.6 8-5.6V7H4zm0 2.8V17h16V9.8l-8 5.6-8-5.6z"/></svg>
        admin@tarvinestates.com.au
      </li>
      <li class="contacts__item">
        <svg class="contacts__icon" viewBox="0 0 24 24"><path d="M12 2a10 10 0 1 0 0 20 10 10 0 0 0 0-20zm0 2c1 0 2.2 1.8 2.7 5H9.3C9.8 5.8 11 4 12 4zM4.3 9h3c-.1.9-.2 2-.2 3s.1 2.1.2 3h-3a8 8 0 0 1 0-6zm5 0h5.4c.1.9.2 2 .2 3s-.1 2.1-.2 3H9.3c-.1-.9-.2-2-.2-3s.1-2.1.2-3zm7.4 0h3a8 8 0 0 1 0 6h-3c.1-.9.2-2 .2-3s-.1-2.1-.2-3zM9.3 17h5.4c-.5 3.2-1.7 5-2.7 5s-2.2-1.8-2.7-5z"/></svg>
        www.tarvinestates.com.au
      </li>
    </ul>

    <div class="footer-rule"></div>
    <div class="services">BUILDING MANAGEMENT - CONCIERGE - CARETAKING - CLEANING</div>
  </section>
</body>
</html>
```